Brisbane IT support business needs our first website

Hi All,

We are after a new website design for our IT solutions and support business.The business name is Harlow Digital Systems Group, or HDSG for short. We provide a range of solutions and services within the IT space.

I would like to utilize the two colours in our business logo I have uploaded.

I understand this is initially for the design only aspect of the site, but I would like to engage the winner to finish coding the website and finalize after also.

Target Market(s)

Other businesses owners and home users.

Industry/Entity Type

Business

Requirements
Must have
• Nice clean and functional design utilizing our business colours from the logo.

```html
<!DOCTYPE html>
<html lang="en">
<head>
<meta charset="utf-8">
<title>HDSG – IT Solutions</title>
<link rel="stylesheet" href="https://fonts.googleapis.com/css2?family=Open+Sans:wght@400;600;700&display=swap">
<style>
:root{
  --navy:#123a5c;
  --navy-deep:#0d2a45;
  --footer:#0f3150;
  --orange:#f07c1e;
  --text:#555;
  --muted:#888;
  --light:#f4f4f4;
  --white:#fff;
}
*{box-sizing:border-box;margin:0;padding:0}
html,body{width:1200px;height:2212px;overflow:hidden}
body{font-family:"Open Sans",Arial,sans-serif;color:var(--text);background:var(--white);font-size:14px}
.site-header{height:72px;display:flex;align-items:center;justify-content:space-between;padding:0 140px}
.brand{display:flex;align-items:center;gap:12px}
.brand-dot{width:46px;height:46px;border-radius:50%;background:var(--navy)}
.brand-name{font-size:32px;font-weight:700;color:var(--orange)}
.main-nav{display:flex;gap:26px}
.main-nav a{font-size:12px;font-weight:600;color:#333;text-decoration:none;text-transform:uppercase}
.main-nav a.active{color:var(--orange)}
.hero{position:relative;height:568px;background:linear-gradient(120deg,#3a4450 0%,#8a8d90 40%,#cfc8c0 70%,#6c6a68 100%);display:flex;flex-direction:column;align-items:center;justify-content:center;color:var(--white);text-align:center}
.hero-title{font-size:42px;font-weight:700;margin-top:40px}
.hero-sub{font-size:20px;margin-top:8px}
.btn{display:inline-block;background:var(--orange);color:var(--white);font-size:13px;font-weight:700;text-transform:uppercase;padding:12px 22px;border-radius:2px}
.hero .btn{margin-top:34px}
.hero-arrow{position:absolute;top:380px;width:40px;height:40px;border-radius:50%;background:rgba(255,255,255,.85)}
.hero-arrow svg{display:block;margin:10px auto}
.hero-arrow.prev{left:142px}.hero-arrow.next{right:142px}
.dots{display:flex;gap:8px;justify-content:center}
.dots span{width:10px;height:10px;border-radius:50%;border:2px solid currentColor}
.dots span.on{background:currentColor}
.hero .dots{margin-top:26px}
.intro{padding:48px 300px 0;text-align:center;line-height:1.8;font-size:14px;height:150px}
.services{display:flex;justify-content:space-between;padding:0 140px;height:290px}
.card{width:290px;background:var(--white);box-shadow:0 1px 4px rgba(0,0,0,.15);position:relative;text-align:center}
.card-photo{height:140px;background:linear-gradient(135deg,#9fb3c8,#e1e7ee)}
.card-icon{position:absolute;top:112px;left:50%;margin-left:-30px;width:60px;height:60px;border-radius:50%;background:var(--navy);border:4px solid var(--white);display:flex;align-items:center;justify-content:center}
.card h3{font-size:15px;color:#222;margin:44px 0 8px}
.card p{font-size:12px;line-height:1.6;padding:0 40px;color:var(--muted)}
.team{height:518px;background:linear-gradient(180deg,var(--navy-deep),#164a72 60%,#0d2a45);color:var(--white);text-align:center;padding-top:30px}
.section-title{font-size:22px;font-weight:600;text-transform:uppercase}
.team-sub{font-size:13px;margin-top:14px;opacity:.85}
.team-grid{display:flex;justify-content:space-between;padding:0 190px;margin-top:36px}
.member{width:170px}
.member-photo{width:150px;height:150px;border-radius:50%;margin:0 auto;border:5px solid var(--white);background:linear-gradient(160deg,#c7ced6,#6d7b8a)}
.member h4{font-size:20px;font-weight:600;margin-top:18px}
.member p{font-size:11px;line-height:1.6;opacity:.85;margin-top:8px}
.team .btn{margin-top:30px}
.testimonials{height:330px;text-align:center;position:relative;padding-top:40px}
.rule{position:absolute;top:68px;left:140px;right:140px;height:2px;background:#cfd6dc}
.quote-badge{position:relative;width:44px;height:44px;border-radius:50%;background:var(--navy);margin:6px auto 0;display:flex;align-items:center;justify-content:center}
.testimonials h2{font-size:26px;font-weight:400;color:var(--navy);margin-top:20px}
.testimonials .lead{font-size:14px;line-height:1.8;padding:0 290px;margin-top:16px}
.testimonials .author{font-size:13px;margin-top:16px}
.testimonials .author b{color:#222}
.testimonials .dots{color:var(--navy);margin-top:18px}
.site-footer{height:342px;background:var(--footer);color:#c9d4de;display:flex;justify-content:space-between;padding:42px 140px 0}
.col{width:200px}
.col h5{font-size:15px;font-weight:600;color:var(--white);text-transform:uppercase;margin-bottom:16px}
.col p{font-size:12px;line-height:1.6}
.contact-line,.tweet{display:flex;gap:10px;align-items:flex-start;font-size:12px;margin-top:10px;line-height:1.5}
.ic{flex:none;width:16px;height:16px}
.tweet small{display:block;color:#7f93a6}
.signup{display:flex;margin-top:18px}
.signup span{flex:1;background:var(--white);color:#999;font-size:11px;padding:8px 10px}
.signup b{background:#5b86b5;color:var(--white);font-size:11px;padding:8px 12px}
.footer-bar{height:48px;background:var(--navy-deep);display:flex;align-items:center;justify-content:space-between;padding:0 140px;color:#9fb0c1;font-size:12px}
.social{display:flex;gap:8px}
.social span{width:22px;height:22px;border-radius:50%;background:#5b86b5}
</style>
</head>
<body>
<header class="site-header">
  <div class="brand"><span class="brand-dot"></span><span class="brand-name">HDSG</span></div>
  <nav class="main-nav">
    <a class="active" href="#">Home</a><a href="#">About Us</a><a href="#">Insurance Products</a><a href="#">Our Team</a><a href="#">Locations</a><a href="#">Contact Us</a>
  </nav>
</header>

<section class="hero" role="img" aria-label="Office photo of a smiling businesswoman with colleagues">
  <h1 class="hero-title">At vero eos et accusamus ducimus</h1>
  <p class="hero-sub">Ipsum is simply dummy text of the printing.</p>
  <span class="btn">Show More</span>
  <div class="dots"><span></span><span class="on"></span><span></span></div>
  <span class="hero-arrow prev"><svg width="20" height="20" viewBox="0 0 20 20"><path d="M12 4l-6 6 6 6" fill="none" stroke="#333" stroke-width="2.5"/></svg></span>
  <span class="hero-arrow next"><svg width="20" height="20" viewBox="0 0 20 20"><path d="M8 4l6 6-6 6" fill="none" stroke="#333" stroke-width="2.5"/></svg></span>
</section>

<p class="intro">Lorem Ipsum is simply dummy text of the printing and typesetting industry. Lorem Ipsum has been the industry's standard dummy text ever since type specimen book it.</p>

<section class="services">
  <article class="card">
    <div class="card-photo" role="img" aria-label="Team meeting photo"></div>
    <span class="card-icon"><svg width="22" height="22" viewBox="0 0 22 22"><rect x="3" y="7" width="16" height="11" rx="1" fill="#fff"/><rect x="8" y="4" width="6" height="4" fill="none" stroke="#fff" stroke-width="2"/></svg></span>
    <h3>Ipsum Dolor Sit Amet</h3>
    <p>Lorem Ipsum is simply dummy text of the printing and typesetting fun text.</p>
  </article>
  <article class="card">
    <div class="card-photo" role="img" aria-label="Person writing at a desk photo"></div>
    <span class="card-icon"><svg width="22" height="22" viewBox="0 0 22 22"><rect x="3" y="3" width="16" height="16" rx="2" fill="none" stroke="#fff" stroke-width="2"/><path d="M8 14l2-4 5-5 2 2-5 5z" fill="#fff"/></svg></span>
    <h3>Ipsum Dolor Sit Amet</h3>
    <p>Lorem Ipsum is simply dummy text of the printing and typesetting fun text.</p>
  </article>
  <article class="card">
    <div class="card-photo" role="img" aria-label="Business handshake photo"></div>
    <span class="card-icon"><svg width="22" height="22" viewBox="0 0 22 22"><rect x="3" y="5" width="16" height="14" rx="1" fill="none" stroke="#fff" stroke-width="2"/><path d="M3 9h16M7 3v4M15 3v4" stroke="#fff" stroke-width="2"/></svg></span>
    <h3>Ipsum Dolor Sit Amet</h3>
    <p>Lorem Ipsum is simply dummy text of the printing and typesetting fun text.</p>
  </article>
</section>

<section class="team" role="group" aria-label="Our team, set over a night city skyline backdrop">
  <h2 class="section-title">Our Team</h2>
  <p class="team-sub">At vero eos et accusamus et iusto odio dignissimos ducimus atque corrupti quos dolores.</p>
  <div class="team-grid">
    <div class="member"><div class="member-photo" role="img" aria-label="Portrait of team member"></div><h4>Dolor sit amet</h4><p>Lorem ipsum dolor sit amet, consectetur adipiscing elit, sed do eiusmod tempor incididunt.</p></div>
    <div class="member"><div class="member-photo" role="img" aria-label="Portrait of team member"></div><h4>Dolor sit amet</h4><p>Lorem ipsum dolor sit amet, consectetur adipiscing elit, sed do eiusmod tempor incididunt.</p></div>
    <div class="member"><div class="member-photo" role="img" aria-label="Portrait of team member"></div><h4>Dolor sit amet</h4><p>Lorem ipsum dolor sit amet, consectetur adipiscing elit, sed do eiusmod tempor incididunt.</p></div>
    <div class="member"><div class="member-photo" role="img" aria-label="Portrait of team member"></div><h4>Dolor sit amet</h4><p>Lorem ipsum dolor sit amet, consectetur adipiscing elit, sed do eiusmod tempor incididunt.</p></div>
  </div>
  <span class="btn">See How It Works</span>
</section>

<section class="testimonials">
  <span class="rule"></span>
  <div class="quote-badge"><svg width="20" height="16" viewBox="0 0 20 16"><path d="M2 16V9c0-5 3-8 7-9v3c-2 1-3 3-3 5h3v8zM11 16V9c0-5 3-8 7-9v3c-2 1-3 3-3 5h3v8z" fill="#fff"/></svg></div>
  <h2>Client Testimonials</h2>
  <p class="lead">Lorem Ipsum is simply dummy text of the printing and typesetting industry. Lorem Ipsum has been the industry's standard dummy text ever since type specimen book it.</p>
  <p class="author">- <b>Daniel Orwell</b>, Company Name</p>
  <div class="dots"><span class="on"></span><span></span><span></span></div>
</section>

<footer class="site-footer">
  <div class="col">
    <h5>What We Do</h5>
    <p>There are many variations of passages of Lorem Ipsum available, but the majority have suffered alteration in some form, by injected humour, or randomised words which don't look even slightly believable. If you are going to use a passage of Lorem.</p>
  </div>
  <div class="col">
    <h5>Contact</h5>
    <p>There are many variations of passages of Lorem Ipsum available, but the majority.</p>
    <div class="contact-line"><svg class="ic" viewBox="0 0 16 16"><path d="M8 1a5 5 0 0 0-5 5c0 4 5 9 5 9s5-5 5-9a5 5 0 0 0-5-5zm0 7a2 2 0 1 1 0-4 2 2 0 0 1 0 4z" fill="#c9d4de"/></svg>Lorem Ipsum</div>
    <div class="contact-line"><svg class="ic" viewBox="0 0 16 16"><rect x="1" y="3" width="14" height="10" fill="none" stroke="#c9d4de" stroke-width="1.5"/><path d="M1 3l7 6 7-6" fill="none" stroke="#c9d4de" stroke-width="1.5"/></svg>info@hdsg-mail.com</div>
    <div class="contact-line"><svg class="ic" viewBox="0 0 16 16"><path d="M4 1l3 3-2 2c1 2 3 4 5 5l2-2 3 3-2 3C7 14 2 9 1 3z" fill="#c9d4de"/></svg>0315 - 555 555</div>
  </div>
  <div class="col">
    <h5>Latest Tweets</h5>
    <div class="tweet"><svg class="ic" viewBox="0 0 16 16"><circle cx="8" cy="8" r="7" fill="#5b86b5"/></svg><div>Lorem Ipsum is simply dummy text of the printing and typesetting industry. Lorem Ipsum<small>1 hour ago</small></div></div>
    <div class="tweet"><svg class="ic" viewBox="0 0 16 16"><circle cx="8" cy="8" r="7" fill="#5b86b5"/></svg><div>Lorem Ipsum is simply dummy text of the printing and typesetting industry.<small>1 hour ago</small></div></div>
  </div>
  <div class="col">
    <h5>News Letter</h5>
    <p>Type your email address below and receive our daily news letter for free.</p>
    <div class="signup"><span>Email Address</span><b>Go</b></div>
  </div>
</footer>
<div class="footer-bar">
  <span>© 2014 All rights reserved. Theme by hdsg-web.com</span>
  <div class="social"><span></span><span></span><span></span><span></span></div>
</div>
</body>
</html>
```